Flyer Design job - Occupational Therapy Flyer!

We are looking for a flyer design.
SPECIFICATIONS:
Size: 8 1/2 x 11, bleeds .125 inches all around.
CMYK colors only. One sided print.

THE COMPANY:
The clientele is an all boys school.
- We do not want any photos of kids, or people.
- Attached is the image we want to use, along with their logo and copy.

Here is the copy as well: Copy for flyer:
The Brookfield Academy is excited to welcome (This is the name of the boys school that will not have occupational services offered in their school).
Tumble Nest OT (logo)
We’re proud to provide your child with professional occupational therapy services right in his school. The familiar environment paired with our expert and caring therapists will give your son the chance to grow and thrive without leaving his comfort zone.
• Mrs. Dalia Feinmoss, OTR/L, Director of Occupational Therapy Services Working in private practice for over 19 years
• Fully equipped therapy gym
• No transportation necessary (no missing Yeshiva or work)
• Introductory low rates for evaluations and therapy sessions
• Communication and collaboration with the parents, Principals, Rebbeim, teachers, and other therapists
• Therapy is exclusive to The Brookfield Academy, servicing boys from primary through eighth grade.

(Highlighted text:) Private therapy in a school setting

Call or email now to schedule your evaluation
555-214-0839 tumblenestot1@mailhaven.test
Tumble Nest OT • PO Box 912 • Harlow NJ 08999

Target Market(s)

Parent of school aged boys. (preschool - 8th grade).

Colors

Designer to choose colors to be used in the design.

Requirements
Must have
• My logo, copy, the image i supplied. It should be well laid out, with nice typography, easy to read, and look fun.
• It must be able to be saved down to CS6. Adobe suite.
• CMYK
Should not have
• It should not look "girly".
• No images of people or kids.

```html
<!DOCTYPE html>
<html lang="en">
<head>
<meta charset="utf-8">
<title>Tumble Nest OT – Flyer</title>
<link rel="stylesheet" href="https://fonts.googleapis.com/css2?family=Noto+Serif&family=Open+Sans:wght@300;400;600;700;800&family=Fira+Sans+Condensed:wght@600&display=swap">
<style>
  :root {
    --magenta: #e5127d;
    --teal: #14a6a2;
    --yellow: #fdc512;
    --ink: #3a3a3a;
    --body: #4a4a4a;
    --paper: #ffffff;
    --gym-top: #dfe3e6;
    --gym-mid: #8c95b8;
    --gym-bottom: #2f3fa8;
  }
  * { box-sizing: border-box; margin: 0; padding: 0; }
  html, body { width: 976px; height: 1200px; overflow: hidden; background: var(--paper); }
  .flyer { position: relative; width: 976px; height: 1200px; background: var(--paper); font-family: "Open Sans", sans-serif; color: var(--body); }

  .gym-photo {
    position: absolute; left: 0; top: 0; width: 976px; height: 607px;
    background: linear-gradient(180deg, var(--gym-top) 0%, #c9ced6 35%, var(--gym-mid) 55%, var(--gym-bottom) 78%, #2a3896 100%);
  }
  .brand-mark {
    position: absolute; right: 40px; top: 118px;
    display: flex; align-items: center; gap: 10px;
    font-family: "Open Sans", sans-serif; font-weight: 800; font-size: 40px; color: var(--teal);
  }
  .brand-mark .dot { width: 22px; height: 22px; border-radius: 50%; background: var(--yellow); }

  .soft-pattern {
    position: absolute; left: 470px; top: 620px; width: 300px; height: 530px;
    background: radial-gradient(ellipse at 50% 50%, rgba(200,200,200,0.35) 0%, rgba(230,230,230,0.15) 50%, rgba(255,255,255,0) 75%);
  }

  .headline {
    position: absolute; left: 52px; top: 636px; width: 610px;
    font-family: "Noto Serif", serif; font-weight: 400; font-size: 45px; line-height: 56px; color: var(--magenta);
    letter-spacing: 0.5px; white-space: nowrap;
  }
  .headline sup { font-size: 32px; vertical-align: 14px; margin-left: 4px; }

  .gym-badge {
    position: absolute; left: 673px; top: 575px; width: 212px; height: 212px; border-radius: 50%;
    background: var(--yellow); display: flex; align-items: center; justify-content: center; text-align: center;
    font-weight: 800; font-size: 31px; line-height: 37px; color: #222;
  }

  .intro {
    position: absolute; left: 52px; top: 778px; width: 520px;
    font-weight: 300; font-size: 15.5px; line-height: 26px; color: var(--body);
  }

  .benefits { position: absolute; left: 52px; top: 904px; width: 445px; list-style: none; }
  .benefits li {
    position: relative; padding-left: 22px; margin-bottom: 9px;
    font-weight: 300; font-size: 13px; line-height: 19px; color: var(--body);
  }
  .benefits li::before {
    content: ""; position: absolute; left: 2px; top: 5px; width: 9px; height: 9px;
    background: var(--magenta); transform: rotate(45deg);
  }

  .tagline { position: absolute; left: 36px; top: 1072px; display: flex; align-items: center; gap: 30px; }
  .tagline .dot { width: 64px; height: 64px; border-radius: 50%; background: var(--yellow); }
  .tagline p { font-family: "Fira Sans Condensed", sans-serif; font-weight: 600; font-size: 33px; line-height: 38px; color: var(--teal); }

  .director { position: absolute; left: 653px; top: 808px; width: 250px; text-align: center; color: var(--ink); }
  .director .name { font-weight: 600; font-size: 19px; line-height: 24px; }
  .director .role { font-weight: 600; font-size: 13px; line-height: 21px; }

  .cta { position: absolute; left: 643px; top: 940px; width: 270px; text-align: center; }
  .cta h2 { font-weight: 600; font-size: 25px; line-height: 32px; color: var(--ink); }
  .cta .phone { margin-top: 10px; font-weight: 700; font-size: 40px; line-height: 46px; color: var(--magenta); white-space: nowrap; margin-left: -30px; margin-right: -30px; }
  .cta .email { font-weight: 600; font-size: 18px; line-height: 26px; color: var(--ink); white-space: nowrap; margin-left: -40px; margin-right: -40px; }

  .footer { position: absolute; left: 0; top: 1158px; width: 976px; height: 42px; }
  .footer svg { position: absolute; left: 0; top: 0; }
  .footnote {
    position: absolute; left: 30px; top: 4px; width: 350px;
    font-size: 11.5px; line-height: 16px; color: #222; text-indent: -8px; padding-left: 10px;
  }
  .address { position: absolute; right: 28px; top: 11px; font-size: 16px; color: #fff; }
</style>
</head>
<body>
<main class="flyer">
  <div class="gym-photo" role="img" aria-label="Therapy gym room with blue mats, a hanging tire swing, trapeze bar, foam steps, a blue tent and a therapy ball"></div>

  <div class="brand-mark"><span class="dot"></span>Tumble Nest OT</div>

  <div class="soft-pattern" role="img" aria-label="Faint grey decorative shapes"></div>

  <h1 class="headline">The Brookfield Academy<sup>*</sup><br>is excited to welcome</h1>

  <div class="gym-badge">Fully<br>equipped<br>therapy<br>gym</div>

  <p class="intro">We’re proud to provide your child with professional occupational therapy services right in his school. The familiar environment paired with our expert and caring therapists will give your son the chance to grow and thrive without leaving his comfort zone.</p>

  <ul class="benefits">
    <li>No transportation necessary (no missing Yeshiva or work)</li>
    <li>Introductory low rates for evaluations and therapy sessions</li>
    <li>Communication and collaboration with the parents, Principals,<br>Rebbeim, teachers, and other therapists</li>
    <li>Therapy is exclusive to the Brookfield Academy, servicing boys from<br>primary through eighth grade.</li>
  </ul>

  <div class="tagline"><span class="dot"></span><p>PRIVATE THERAPY<br>In A School Setting</p></div>

  <div class="director">
    <p class="name">Mrs. Dalia Feinmoss,</p>
    <p class="role">OTR/L, Director of Occupational<br>Therapy Services Working in private<br>practice for over 19 years</p>
  </div>

  <div class="cta">
    <h2>Call or email now to<br>schedule your<br>evaluation</h2>
    <p class="phone">555-214-0839</p>
    <p class="email">tumblenestot1@mailhaven.test</p>
  </div>

  <footer class="footer">
    <svg width="976" height="42" viewBox="0 0 976 42" aria-hidden="true">
      <rect x="0" y="0" width="976" height="42" fill="var(--teal)"/>
      <polygon points="0,0 495,0 520,42 0,42" fill="var(--yellow)"/>
    </svg>
    <p class="footnote">* This is the name of the boys school that will not have occupational services offered in their school</p>
    <p class="address">Tumble Nest OT • PO Box 912 • Harlow NJ 08999</p>
  </footer>
</main>
</body>
</html>
```